Vantro #27 - MEN'S NATURAL THERAPEUTIC INTIMATE WASH

Men's Natural Therapeutic INTIMATE Wash
VANTRO #27

Design a 4 oz. stand up tube with flip top cap...
To be packaged in a carton/box

Formula contains Tea Tree OIL
Aloe Vera Gel
Coconut Oil

PRODUCT IS A WASH/SOAP

Helps with
- Jock Itch (tinea cruris)
- Skin Rashes
- Candida
- Itchy Skin

COLORS ON TUBE: Gray, Black, Lime Electric Green and Blue

PRODUCT FOR MEN!

Target Market(s)

MEN

Industry/Entity Type

Retail

Font styles to use
Sans Serif

Colors
9bcb3b
abd036
33a6d7
000000
c9c9c9

Requirements
Must have
• Colors... black, gray, electric green and blue
Nice to have
• Needs to look masculine appeal to the male consumer

```html
<!DOCTYPE html>
<html lang="en">
<head>
<meta charset="utf-8">
<title>Vantro #27 – Men's Natural Therapeutic Intimate Wash</title>
<link href="https://fonts.googleapis.com/css2?family=Marcellus&family=Oswald:wght@400;500&display=swap" rel="stylesheet">
<style>
  :root {
    --bg-top: #ffffff;
    --bg-bottom: #ececec;
    --tube-body: #2e2e30;
    --tube-rim: #111112;
    --cap: #0f0f10;
    --label-gray: #d6d6d6;
    --stripe-dark: #232325;
    --ink: #1a1a1a;
    --white: #ffffff;
    --green: #9bcb3b;
    --lime: #abd036;
    --sky: #33a6d7;
    --blue: #2c62dd;
  }
  * { margin: 0; padding: 0; box-sizing: border-box; }
  html, body { width: 1200px; height: 687px; overflow: hidden; }
  body {
    position: relative;
    background: linear-gradient(var(--bg-top), var(--bg-bottom));
  }
  .tube {
    position: absolute;
    top: 42px;
    width: 256px;
    height: 450px;
  }
  .tube--green { left: 55px; --accent: var(--green); }
  .tube--lime { left: 333px; --accent: var(--lime); }
  .tube--sky { left: 612px; --accent: var(--sky); }
  .tube--blue { left: 889px; --accent: var(--blue); }

  .tube__shape { position: absolute; inset: 0; }
  .tube__body { fill: var(--tube-body); }
  .tube__rim { fill: var(--tube-rim); }
  .tube__label { fill: var(--label-gray); }
  .tube__stripe { fill: var(--stripe-dark); }
  .tube__band { fill: var(--accent); }
  .tube__cap { fill: var(--cap); }

  .brand-name {
    position: absolute;
    top: 162px;
    left: 0;
    width: 256px;
    text-align: center;
    font-family: "Marcellus", serif;
    font-size: 25px;
    letter-spacing: 0.5px;
    color: var(--ink);
  }
  .formula {
    position: absolute;
    top: 268px;
    left: 50px;
    width: 30px;
    text-align: center;
    font-family: "Oswald", sans-serif;
    color: var(--white);
    line-height: 1;
  }
  .formula__prefix {
    display: block;
    font-family: "Marcellus", serif;
    font-size: 9px;
    padding-bottom: 2px;
    border-bottom: 1px solid var(--white);
    margin-bottom: 2px;
  }
  .formula__number { display: block; font-size: 17px; font-weight: 500; }
  .divider {
    position: absolute;
    top: 262px;
    left: 84px;
    width: 1.5px;
    height: 44px;
    background: var(--white);
  }
  .product-name {
    position: absolute;
    top: 263px;
    left: 92px;
    font-family: "Oswald", sans-serif;
    font-weight: 500;
    font-size: 11.5px;
    line-height: 14px;
    color: var(--white);
    white-space: nowrap;
  }
</style>
</head>
<body>

  <div class="tube tube--green">
    <svg class="tube__shape" viewBox="0 0 256 450" width="256" height="450">
      <defs>
        <clipPath id="body-green"><polygon points="0,4 256,4 205,364 51,364"/></clipPath>
        <linearGradient id="sheen-green" x1="0" y1="0" x2="1" y2="1">
          <stop offset="0" stop-color="#ffffff" stop-opacity="0.12"/>
          <stop offset="0.5" stop-color="#ffffff" stop-opacity="0.02"/>
          <stop offset="1" stop-color="#000000" stop-opacity="0.1"/>
        </linearGradient>
      </defs>
      <g clip-path="url(#body-green)">
        <rect class="tube__body" x="0" y="0" width="256" height="364"/>
        <rect class="tube__label" x="0" y="108" width="256" height="138"/>
        <rect class="tube__stripe" x="0" y="246" width="256" height="9"/>
        <rect class="tube__band" x="0" y="255" width="256" height="55"/>
        <rect x="0" y="0" width="256" height="246" fill="url(#sheen-green)" role="img" aria-label="Faceted geometric texture across the upper tube"/>
      </g>
      <rect class="tube__rim" x="0" y="0" width="256" height="10" rx="4"/>
      <path class="tube__cap" d="M48,364 H208 L211,440 Q211,448 203,448 H53 Q45,448 45,440 Z"/>
    </svg>
    <p class="brand-name">BRAND NAME</p>
    <p class="formula"><span class="formula__prefix">NO.</span><span class="formula__number">27</span></p>
    <span class="divider"></span>
    <p class="product-name">Men's<br>Natural Therapeutic<br>INTIMATE Wash</p>
  </div>

  <div class="tube tube--lime">
    <svg class="tube__shape" viewBox="0 0 256 450" width="256" height="450">
      <defs>
        <clipPath id="body-lime"><polygon points="0,4 256,4 205,364 51,364"/></clipPath>
        <linearGradient id="sheen-lime" x1="0" y1="0" x2="1" y2="1">
          <stop offset="0" stop-color="#ffffff" stop-opacity="0.12"/>
          <stop offset="0.5" stop-color="#ffffff" stop-opacity="0.02"/>
          <stop offset="1" stop-color="#000000" stop-opacity="0.1"/>
        </linearGradient>
      </defs>
      <g clip-path="url(#body-lime)">
        <rect class="tube__body" x="0" y="0" width="256" height="364"/>
        <rect class="tube__label" x="0" y="108" width="256" height="138"/>
        <rect class="tube__stripe" x="0" y="246" width="256" height="9"/>
        <rect class="tube__band" x="0" y="255" width="256" height="55"/>
        <rect x="0" y="0" width="256" height="246" fill="url(#sheen-lime)" role="img" aria-label="Faceted geometric texture across the upper tube"/>
      </g>
      <rect class="tube__rim" x="0" y="0" width="256" height="10" rx="4"/>
      <path class="tube__cap" d="M48,364 H208 L211,440 Q211,448 203,448 H53 Q45,448 45,440 Z"/>
    </svg>
    <p class="brand-name">BRAND NAME</p>
    <p class="formula"><span class="formula__prefix">NO.</span><span class="formula__number">27</span></p>
    <span class="divider"></span>
    <p class="product-name">Men's<br>Natural Therapeutic<br>INTIMATE Wash</p>
  </div>

  <div class="tube tube--sky">
    <svg class="tube__shape" viewBox="0 0 256 450" width="256" height="450">
      <defs>
        <clipPath id="body-sky"><polygon points="0,4 256,4 205,364 51,364"/></clipPath>
        <linearGradient id="sheen-sky" x1="0" y1="0" x2="1" y2="1">
          <stop offset="0" stop-color="#ffffff" stop-opacity="0.12"/>
          <stop offset="0.5" stop-color="#ffffff" stop-opacity="0.02"/>
          <stop offset="1" stop-color="#000000" stop-opacity="0.1"/>
        </linearGradient>
      </defs>
      <g clip-path="url(#body-sky)">
        <rect class="tube__body" x="0" y="0" width="256" height="364"/>
        <rect class="tube__label" x="0" y="108" width="256" height="138"/>
        <rect class="tube__stripe" x="0" y="246" width="256" height="9"/>
        <rect class="tube__band" x="0" y="255" width="256" height="55"/>
        <rect x="0" y="0" width="256" height="246" fill="url(#sheen-sky)" role="img" aria-label="Faceted geometric texture across the upper tube"/>
      </g>
      <rect class="tube__rim" x="0" y="0" width="256" height="10" rx="4"/>
      <path class="tube__cap" d="M48,364 H208 L211,440 Q211,448 203,448 H53 Q45,448 45,440 Z"/>
    </svg>
    <p class="brand-name">BRAND NAME</p>
    <p class="formula"><span class="formula__prefix">NO.</span><span class="formula__number">27</span></p>
    <span class="divider"></span>
    <p class="product-name">Men's<br>Natural Therapeutic<br>INTIMATE Wash</p>
  </div>

  <div class="tube tube--blue">
    <svg class="tube__shape" viewBox="0 0 256 450" width="256" height="450">
      <defs>
        <clipPath id="body-blue"><polygon points="0,4 256,4 205,364 51,364"/></clipPath>
        <linearGradient id="sheen-blue" x1="0" y1="0" x2="1" y2="1">
          <stop offset="0" stop-color="#ffffff" stop-opacity="0.12"/>
          <stop offset="0.5" stop-color="#ffffff" stop-opacity="0.02"/>
          <stop offset="1" stop-color="#000000" stop-opacity="0.1"/>
        </linearGradient>
      </defs>
      <g clip-path="url(#body-blue)">
        <rect class="tube__body" x="0" y="0" width="256" height="364"/>
        <rect class="tube__label" x="0" y="108" width="256" height="138"/>
        <rect class="tube__stripe" x="0" y="246" width="256" height="9"/>
        <rect class="tube__band" x="0" y="255" width="256" height="55"/>
        <rect x="0" y="0" width="256" height="246" fill="url(#sheen-blue)" role="img" aria-label="Faceted geometric texture across the upper tube"/>
      </g>
      <rect class="tube__rim" x="0" y="0" width="256" height="10" rx="4"/>
      <path class="tube__cap" d="M48,364 H208 L211,440 Q211,448 203,448 H53 Q45,448 45,440 Z"/>
    </svg>
    <p class="brand-name">BRAND NAME</p>
    <p class="formula"><span class="formula__prefix">NO.</span><span class="formula__number">27</span></p>
    <span class="divider"></span>
    <p class="product-name">Men's<br>Natural Therapeutic<br>INTIMATE Wash</p>
  </div>

</body>
</html>
```